Quillmere Financial Plans

I am looking for a complete resdesign of my small financial presentation. This is a Word Doc/PDF that I print off when meeting with people in private. I often present my "two pager" that I have been using for years and years. It tells them the basics of what I do, how I help people and foundational financial principles.

I have recently gone out on my own in business and have completely rebranded. This presentation is my most used tool, so it is the first of many things I would like to redo. I am hoping it will somehow coordinate with the colors of my business, not necessarily the EXACT same 3 colors everywhere, but have the design colors compliment.

I've uploaded all my logo designs, as well as the current "two-pager". I am not against it going to 3 pages if needed. As it will still land on 2 pages with duplex printing.

It has always been VERY simple. I am wanting it built into a more professional and design specific format, to show off my branding, without being over cluttered.

I am completely open to ANY graphics changes. Obviously some are very novice, the house on the last page has always been overly simplified.

```html
<!DOCTYPE html>
<html lang="en">
<head>
<meta charset="utf-8">
<title>Quillmere Financial Plans – Two Pager</title>
<link href="https://fonts.googleapis.com/css2?family=Poppins:wght@600;700;800&family=Roboto:wght@400;500;700&display=swap" rel="stylesheet">
<style>
:root{
  --backdrop:#767f78;
  --navy:#0c1d2d;
  --green:#19a84a;
  --grey-band:#878d93;
  --line:#24384c;
  --white:#ffffff;
  --ink:#1b1f24;
  --cell-line:#c9ced2;
}
*{box-sizing:border-box;margin:0;padding:0}
html,body{width:1200px;height:1008px;overflow:hidden}
body{background:var(--backdrop);font-family:Roboto,Arial,sans-serif;position:relative}
.page{position:absolute;width:538px;height:740px;overflow:hidden}
.abs{position:absolute}
.banner{position:absolute;display:flex;align-items:center;justify-content:center;font-family:Poppins,sans-serif;font-weight:800;color:var(--white);text-transform:uppercase}

/* page one */
.page-one{left:49px;top:96px;background:var(--navy)}
.brand-name{left:0;width:538px;top:38px;text-align:center;font-family:Poppins,sans-serif;font-weight:600;color:var(--white);font-size:20px;letter-spacing:2px}
.challenge{left:49px;top:96px;width:440px;height:58px;background:var(--green);font-size:21px}
.facts{left:35px;top:154px;width:468px;height:231px;border:1px solid var(--line);border-top:none}
.facts .divider{position:absolute;top:0;bottom:0;width:1px;background:var(--line)}
.col-head{position:absolute;top:18px;font-family:Poppins,sans-serif;font-weight:800;font-size:12px;color:var(--white)}
.fact{position:absolute;font-size:5.6px;line-height:8.8px;color:var(--white);text-transform:uppercase}
.source{position:absolute;font-size:5.6px;line-height:8.8px;color:var(--green);font-weight:700;text-transform:uppercase}
.ring{position:absolute;width:21px;height:21px;border-radius:50%;border:2px solid var(--white);border-right-color:var(--green);border-bottom-color:var(--green);display:flex;align-items:center;justify-content:center;font-size:6.2px;font-weight:700;color:var(--white)}
.dot-mark{position:absolute;width:18px;height:18px;border-radius:50%;border:2px solid #8c959c}
.who{left:103px;top:385px;width:333px;height:36px;background:var(--grey-band);font-size:13.5px}
.service{position:absolute;top:441px;width:78px;text-align:center;font-size:6.8px;font-weight:700;color:var(--white);line-height:9.5px}
.service .icon{width:32px;height:32px;border-radius:50%;border:1.5px solid #9aa3aa;margin:0 auto 5px;display:flex;align-items:center;justify-content:center;color:#b9c1c6;font-size:13px;font-weight:700}
.service .label{height:19px;display:flex;align-items:flex-end;justify-content:center}
.glow{left:0;top:520px;width:538px;height:60px;background:radial-gradient(ellipse at 50% 40%,rgba(25,168,74,.25),rgba(25,168,74,0) 65%)}
.pill{position:absolute;border-radius:14px;background:var(--green);color:var(--white);font-weight:500;display:flex;align-items:center;justify-content:center;gap:7px}
.pill .knob{width:17px;height:17px;border-radius:50%;background:var(--white);border:3px solid var(--green);box-shadow:0 0 0 1.5px var(--white)}
.education{left:189px;top:511px;width:160px;height:24px;font-size:9px}
.how{left:103px;top:565px;width:333px;height:35px;background:var(--green);font-size:13.5px}
.chart{left:18px;top:616px}
.chart-label{position:absolute;font-size:6.8px;color:var(--white);line-height:8.5px;text-align:center}
.checks{left:170px;top:628px}
.checks li{list-style:none;display:flex;align-items:center;gap:6px;font-size:6.8px;color:var(--white);height:24.5px}
.checks li::before{content:"";width:6px;height:6px;background:var(--white)}
.savings-tag{left:132px;top:632px;font-size:6.8px;color:var(--green);font-weight:700}
.badges{left:307px;top:622px;display:grid;grid-template-columns:47px 49px;grid-auto-rows:16px;column-gap:3px;row-gap:3px}
.badges span{background:#d9e9f4;border-radius:5px}
.pay{left:444px;top:658px;width:74px;height:24px;font-size:9px}
.page-no{position:absolute;font-size:6.5px;font-weight:700;color:var(--white)}

/* page two */
.page-two{left:613px;top:172px;background:linear-gradient(180deg,#dde1e5 0%,#eef0f2 45%,#e4e7ea 100%)}
.page-two .sheen{left:0;top:230px;width:538px;height:150px;background:linear-gradient(175deg,rgba(255,255,255,0) 0%,rgba(255,255,255,.7) 45%,rgba(200,206,212,.5) 100%)}
.rule{left:182px;top:0;width:175px;height:38px;background:var(--green);font-size:20px}
.doubling{position:absolute;top:54px;width:123px;border-collapse:collapse;font-size:8px;color:var(--ink)}
.doubling th{background:var(--navy);color:var(--white);font-weight:500;height:26px;padding:0 11px}
.doubling td{background:var(--white);height:26.6px;border:1px solid var(--cell-line);padding:0 8px}
.doubling th:first-child,.doubling td:first-child{text-align:left;width:60px}
.doubling th:last-child,.doubling td:last-child{text-align:right}
.doubles{position:absolute;top:291px;display:flex;gap:6px;align-items:center;font-size:8.2px;font-weight:500;color:#2a3036;line-height:11px}
.doubles .dot-mark{position:static;border-color:#7c858b;width:20px;height:20px}
.arch{left:0;top:0}
.taxes{left:182px;top:337px;width:175px;height:38px;background:var(--green);font-size:21px}
.tax-col{position:absolute;top:432px;color:var(--white)}
.tax-col h3{font-family:Roboto,sans-serif;font-weight:500;font-size:11px;margin-bottom:10px}
.tax-col ul{list-style:none}
.tax-col li{position:relative;padding-left:13px;font-size:9.3px;line-height:13px;margin-bottom:9.5px}
.tax-col li::before{content:"";position:absolute;left:1px;top:4px;width:4px;height:4px;border-radius:50%;background:var(--green)}
.tax-rule{position:absolute;width:1px;top:424px;height:156px;background:rgba(255,255,255,.15)}
.tax-result{position:absolute;top:550px;font-family:Poppins,sans-serif;font-weight:700;font-size:14px;color:var(--white)}
.closing{position:absolute;top:609px;width:260px;height:63px;display:flex;align-items:center;justify-content:center;text-align:center;font-family:Poppins,sans-serif;font-weight:700;font-size:16px;line-height:19.5px;text-transform:uppercase}
.closing.navy{left:10px;background:var(--navy);color:var(--white)}
.closing.green{left:270px;background:var(--green);color:var(--navy)}
</style>
</head>
<body>

<section class="page page-one">
  <div class="abs brand-name">QUILLMERE FINANCIAL PLANS</div>

  <div class="banner challenge">The Financial Challenge</div>

  <div class="abs facts">
    <span class="divider" style="left:155px"></span>
    <span class="divider" style="left:311px"></span>

    <h2 class="col-head" style="left:14px">SAVINGS</h2>
    <span class="ring" style="left:16px;top:47px">49%</span>
    <p class="fact" style="left:42px;top:49px">Canadian employees are<br>&nbsp;living paycheque to paycheque.</p>
    <span class="ring" style="left:16px;top:76px">25%</span>
    <p class="fact" style="left:42px;top:77px">Canadians are unable to cover<br>an unexpected $500 expense</p>
    <p class="source" style="left:39px;top:99px">- National Stats Office (Feb 2023)</p>
    <span class="ring" style="left:16px;top:116px">25%</span>
    <p class="fact" style="left:42px;top:117px">Canadians need to access<br>their retirement savings early.</p>
    <span class="ring" style="left:16px;top:144px">20%</span>
    <p class="fact" style="left:42px;top:149px">Canadians have no savings.</p>
    <span class="ring" style="left:16px;top:171px">39%</span>
    <p class="fact" style="left:42px;top:173px">Canadians aged 55-65 have less<br>than $5,000 in savings.</p>
    <p class="source" style="left:39px;top:197px">-Federal Review Office<br>(June 2023)</p>

    <h2 class="col-head" style="left:170px">DEBT</h2>
    <span class="dot-mark" style="left:172px;top:48px"></span>
    <p class="fact" style="left:197px;top:49px">The average Canadian has<br>$22,131 in consumer debt.<br>Which excludes mortgages</p>
    <p class="source" style="left:194px;top:78px">- Creditwell (Aug 2024)</p>
    <span class="dot-mark" style="left:172px;top:95px"></span>
    <p class="fact" style="left:197px;top:96px">Over 55% of Canadians hold<br>credit card debt and the total<br>Canadian household debt has<br>increased to $2.52trillion,<br>including consumer credit,<br>mortgage and non-mortgage<br>loans.</p>
    <p class="source" style="left:194px;top:161px">- National Lenders Assoc.<br>(Aug 2024</p>

    <h2 class="col-head" style="left:326px">INSURANCE</h2>
    <span class="ring" style="left:326px;top:47px">45%</span>
    <p class="fact" style="left:353px;top:49px">Canadians do not have individual<br>life insurance coverage,</p>
    <span class="ring" style="left:326px;top:76px">48%</span>
    <p class="fact" style="left:353px;top:77px">Say their families would face<br>financial trouble within 6<br>months of losing someone</p>
    <p class="source" style="left:350px;top:105px">-Lifeview Intl. (Apr 2023)</p>
    <span class="dot-mark" style="left:328px;top:118px"></span>
    <p class="fact" style="left:353px;top:117px">2-in-5 Canadians (43% women / 44%<br>men) will be diagosed with a form<br>of cancer or other critical<br>illness during their lifetime. Every<br>7 seconds</p>
    <p class="source" style="left:350px;top:166px">-Health Data Portal<br>(June 2024)</p>
  </div>

  <div class="banner who">Who are we and what do we do?</div>

  <div class="service" style="left:36px"><div class="icon">$</div><div class="label">CASH FLOW</div></div>
  <div class="service" style="left:114px"><div class="icon">$</div><div class="label">CASH FLOW<br>PROTECTION</div></div>
  <div class="service" style="left:192px"><div class="icon">%</div><div class="label">DEBT<br>MANAGEMENT</div></div>
  <div class="service" style="left:270px"><div class="icon">$</div><div class="label">EMERGENCY<br>FUND</div></div>
  <div class="service" style="left:348px"><div class="icon">↑</div><div class="label">BUILD WEALTH</div></div>
  <div class="service" style="left:426px"><div class="icon">✓</div><div class="label">PRESERVE</div></div>

  <div class="abs glow"></div>
  <div class="pill education">EDUCATION &amp; AWARENESS <span class="knob"></span></div>

  <div class="banner how">How are we doing it?</div>

  <svg class="abs chart" width="112" height="112" viewBox="0 0 112 112" aria-hidden="true">
    <circle cx="55" cy="53" r="51" fill="none" stroke="#8a9298" stroke-width="2.5"/>
    <line x1="55" y1="2" x2="55" y2="104" stroke="var(--green)" stroke-width="2.5"/>
    <line x1="55" y1="52" x2="106" y2="52" stroke="var(--green)" stroke-width="2.5"/>
    <line x1="55" y1="52" x2="100" y2="30" stroke="#8a9298" stroke-width=".8"/>
    <line x1="55" y1="52" x2="100" y2="58" stroke="#8a9298" stroke-width=".8"/>
  </svg>
  <span class="chart-label" style="left:36px;top:664px">LIVING<br>EXPENSES</span>
  <span class="chart-label" style="left:84px;top:650px">TAXES</span>
  <span class="chart-label" style="left:84px;top:683px">DEBT</span>
  <span class="abs savings-tag">SAVINGS</span>

  <svg class="abs" style="left:128px;top:665px" width="440" height="10" aria-hidden="true">
    <line x1="0" y1="4" x2="30" y2="4" stroke="#fff" stroke-width="1" stroke-dasharray="2 2"/>
    <path d="M30 1 L36 4 L30 7 Z" fill="#fff"/>
    <line x1="188" y1="4" x2="222" y2="4" stroke="#fff" stroke-width="1" stroke-dasharray="2 2"/>
    <path d="M222 1 L228 4 L222 7 Z" fill="#fff"/>
    <line x1="282" y1="4" x2="309" y2="4" stroke="#fff" stroke-width="1" stroke-dasharray="2 2"/>
    <path d="M309 1 L315 4 L309 7 Z" fill="#fff"/>
  </svg>

  <ul class="abs checks">
    <li>RETIREMENT SAVINGS</li>
    <li>CHILDREN'S EDUCATION</li>
    <li>PROPER PROTECTION</li>
    <li>FREEDOM FROM DEBT</li>
  </ul>

  <div class="abs badges" role="img" aria-label="Partner insurer badges">
    <span></span><span></span><span></span><span></span><span></span><span></span><span></span><span></span><span></span><span></span>
  </div>

  <div class="pill pay">PAY US <span class="knob"></span></div>
  <span class="page-no" style="left:503px;top:722px">Page 01</span>
</section>

<section class="page page-two">
  <div class="abs sheen" role="img" aria-label="Soft flowing silver wave texture"></div>

  <div class="banner rule">Rule of 72</div>

  <table class="doubling" style="left:20px">
    <tr><th>AGE</th><th>4%</th></tr>
    <tr><td>29</td><td>$10,000</td></tr>
    <tr><td>47</td><td>$20,000</td></tr>
    <tr><td>65</td><td>$40,000</td></tr>
  </table>
  <table class="doubling" style="left:145px">
    <tr><th>AGE</th><th>6%</th></tr>
    <tr><td>29</td><td>$10,000</td></tr>
    <tr><td>41</td><td>$20,000</td></tr>
    <tr><td>53</td><td>$40,000</td></tr>
    <tr><td>65</td><td>$80,000</td></tr>
  </table>
  <table class="doubling" style="left:270px">
    <tr><th>AGE</th><th>8%</th></tr>
    <tr><td>29</td><td>$10,000</td></tr>
    <tr><td>38</td><td>$20,000</td></tr>
    <tr><td>47</td><td>$40,000</td></tr>
    <tr><td>56</td><td>$80,000</td></tr>
    <tr><td>65</td><td>$160,000</td></tr>
  </table>
  <table class="doubling" style="left:395px">
    <tr><th>AGE</th><th>8%</th></tr>
    <tr><td>29</td><td>$10,000</td></tr>
    <tr><td>35</td><td>$20,000</td></tr>
    <tr><td>41</td><td>$40,000</td></tr>
    <tr><td>47</td><td>$80,000</td></tr>
    <tr><td>53</td><td>$160,000</td></tr>
    <tr><td>59</td><td>$320,000</td></tr>
    <tr><td>65</td><td>$640,000</td></tr>
  </table>

  <div class="doubles" style="left:36px"><span class="dot-mark"></span><span>MONEY DOUBLES<br>EVERY 18 YEARS</span></div>
  <div class="doubles" style="left:158px"><span class="dot-mark"></span><span>MONEY DOUBLES<br>EVERY 18 YEARS</span></div>
  <div class="doubles" style="left:280px"><span class="dot-mark"></span><span>MONEY DOUBLES<br>EVERY 18 YEARS</span></div>
  <div class="doubles" style="left:402px"><span class="dot-mark"></span><span>MONEY DOUBLES<br>EVERY 18 YEARS</span></div>

  <svg class="abs arch" width="538" height="740" viewBox="0 0 538 740" role="img" aria-label="Dark green field with flowing line waves">
    <defs>
      <linearGradient id="fieldTone" x1="0" y1="0" x2="0" y2="1">
        <stop offset="0" stop-color="#1e3a2c"/>
        <stop offset=".55" stop-color="#1f4432"/>
        <stop offset=".8" stop-color="#1d6a44"/>
        <stop offset="1" stop-color="#17553a"/>
      </linearGradient>
    </defs>
    <path d="M0 427 Q270 230 538 425" fill="none" stroke="#8f959a" stroke-width="7"/>
    <path d="M0 433 Q270 240 538 431 L538 740 L0 740 Z" fill="url(#fieldTone)"/>
  </svg>

  <div class="banner taxes">Taxes</div>

  <span class="tax-rule" style="left:146px"></span>
  <span class="tax-rule" style="left:260px"></span>
  <span class="tax-rule" style="left:399px"></span>

  <div class="tax-col" style="left:19px">
    <h3>HOME</h3>
    <ul><li>Partner with mortgage<br>Brokers for Best rates</li><li style="margin-top:14px">Mortgage Insurance<br>alternatives</li></ul>
  </div>
  <div class="tax-col" style="left:167px">
    <h3>RRSP</h3>
    <ul><li>Tax Deduction</li><li>Tax Deferred</li></ul>
  </div>
  <div class="tax-col" style="left:273px">
    <h3>TFSA</h3>
    <ul><li>No Tax Deductions</li><li>Tax Free Growth</li><li>2009-$95,000</li><li>LIMIT 2023-$7,000/YR</li></ul>
  </div>
  <div class="tax-col" style="left:418px">
    <h3>PREM LIFE</h3>
    <ul><li>No Tax Deductions</li><li>Qualify</li><li>Tax Deffered Growth</li></ul>
  </div>

  <span class="tax-result" style="left:36px">SELL</span>
  <span class="tax-result" style="left:167px">100% TAX</span>
  <span class="tax-result" style="left:273px">0% TAX</span>
  <span class="tax-result" style="left:418px">0% TAX</span>

  <div class="closing navy">Life Insurance Illness<br>Critical/Disabilitty</div>
  <div class="closing green">Debt Management<br>Cash Flow</div>

  <span class="page-no" style="left:503px;top:720px">Page 02</span>
</section>

</body>
</html>
```